Tovenly Website Redesign

We have a web site called tovenly.com that is all about education/information about legal marijuana. We're looking to significantly improve the modern-ness and look/feel of the web site - and to make it look like many of the best web sites out there today.

The task will be to come up with a better design for:
- The home page: http://tovenly.com/
- The logo (see the logo at the top of each page)
- The header and footer (for all the pages)
- The vaporizer page: http://tovenly.com/collections/vaporizer
- The store map page: http://tovenly.com/pages/shop-marijuana-in-colorado-state

The output of the project will be:
- screenshots of the designs and any images needed
- PSD file

Key requirements:
- Style needs to look fresh/modern
- Especially on the vaporizers page, the key things we want to drive is conversion - getting more people to interact with the page and actually click on the links to purchase vaporizers

Reason: Raised the budget and want to give designers a few more days to provide entries.

Note I clarified that I don't need code (HTML or CSS) for the project. I just need the designs, including images and the PSD file. Thanks.

Reason: We're getting closet to selecting a design, just need a few more days to iterate on a few we're working on.

Industry/Entity Type

Education

Font styles to use
Sans Serif

Requirements
Must have
• Must look like a modern/clean/fresh looking website design.

```html
<!DOCTYPE html>
<html lang="en">
<head>
<meta charset="utf-8">
<title>Tovenly – Shop marijuana in style</title>
<link href="https://fonts.googleapis.com/css2?family=Roboto+Condensed:wght@400;700&display=swap" rel="stylesheet">
<style>
:root{
  --teal:#0f8a80;
  --teal-dark:#0b6f67;
  --teal-deep:#0a4a45;
  --green:#3cb94a;
  --green-bright:#5fd36b;
  --mint:#e9fcef;
  --paper:#f4f4f4;
  --line:#cfd8d3;
  --text:#2b2b2b;
  --muted:#555;
  --white:#fff;
}
*{box-sizing:border-box;margin:0;padding:0}
html,body{width:747px;height:1200px;overflow:hidden}
body{position:relative;font-family:"Roboto Condensed",Arial,sans-serif;color:var(--text);background:var(--paper)}
.abs{position:absolute}
.logo{left:70px;top:22px;width:180px}
.logo-name{font-weight:700;font-size:36px;color:var(--green);letter-spacing:.5px;line-height:1}
.logo-tag{font-size:10px;color:#333;text-align:right;margin-top:4px}
.ad{left:296px;top:21px;width:384px;height:57px;background:#e2e2e2;border:1px solid #b9e3bf;display:flex;align-items:center;justify-content:center;font-size:15px;color:#222}
.nav{left:66px;top:90px;width:615px;height:35px;background:linear-gradient(#15988d,var(--teal-dark));border-radius:5px 5px 0 0;display:flex;align-items:center;color:var(--white);font-size:11.5px}
.nav-home{width:40px;height:35px;display:flex;align-items:center;justify-content:center}
.nav-item{height:35px;display:flex;align-items:center;padding:0 23px;border-left:1px solid rgba(255,255,255,.18)}
.search{left:552px;top:101px;width:116px;height:15px;background:var(--white);border-radius:8px;font-size:8px;color:var(--teal);display:flex;align-items:center;padding-left:8px;gap:6px}
.hero{left:66px;top:125px;width:615px;height:227px;background:linear-gradient(135deg,#a89a86 0%,#8b8577 45%,#6f7a52 75%,#4f5a3a 100%)}
.main-bg{left:0;top:352px;width:747px;height:704px;background:var(--mint)}
.panel-head{background:linear-gradient(#16998e,var(--teal-dark));color:var(--white);font-size:11.5px;height:30px;display:flex;align-items:center;padding-left:12px;border-radius:5px 5px 0 0}
.panel-box{background:var(--white);border:1px solid var(--line);border-top:none}
.quick{left:67px;top:372px;width:143px}
.quick ul{list-style:none;padding:3px 13px 6px 12px;height:301px}
.quick li{font-size:8.6px;height:23px;line-height:23px;border-bottom:1px dashed #c9c9c9;padding-left:8px;position:relative}
.quick li:last-child{border-bottom:none}
.quick li::before{content:"›";position:absolute;left:0;color:var(--green);font-size:10px}
.reach{left:67px;top:722px;width:143px}
.reach .panel-box{height:91px;display:flex;flex-direction:column;align-items:center;padding-top:16px}
.reach-mail{font-size:12px;margin-top:8px}
.botd{left:223px;top:372px;width:457px}
.botd .panel-head{padding-left:0;justify-content:space-between;padding-right:12px}
.botd-label{background:linear-gradient(#4fcf5b,var(--green));height:30px;width:100px;display:flex;align-items:center;justify-content:center;border-radius:5px 0 0 0}
.botd .panel-box{height:148px;display:flex;gap:12px;padding:11px 11px 0 11px}
.botd-card{width:136px;font-size:8.3px;line-height:11.5px}
.botd-img{height:91px;margin-bottom:5px}
.allblog{left:223px;top:572px;width:457px}
.allblog .panel-head{justify-content:space-between;padding-right:12px}
.pager{display:flex;gap:7px;align-items:center;font-size:11px}
.pager .current{color:var(--green-bright)}
.post{left:223px;width:457px;height:133px;background:var(--white);border:1px solid var(--line)}
.post-img{position:absolute;left:9px;top:9px;width:160px;height:113px;border:3px solid #b5b5b5}
.post-title{position:absolute;left:180px;top:16px;width:260px;color:var(--green);font-size:13px;line-height:17px;font-weight:700}
.post-text{position:absolute;left:180px;width:262px;font-size:8.3px;line-height:12px}
.footer{left:0;top:1056px;width:747px;height:118px;background:var(--teal);color:var(--white)}
.foot-h{font-size:14px;position:absolute;top:23px}
.foot-small{font-size:7.5px;position:absolute;line-height:12.8px}
.divider{position:absolute;top:21px;width:1px;height:75px;background:rgba(255,255,255,.2)}
.social{position:absolute;top:47px;width:20px;height:20px;border-radius:50%;background:#f1f1f1;border:2px solid rgba(255,255,255,.5)}
.copy{left:0;top:1174px;width:747px;height:26px;background:var(--teal-deep);color:var(--green-bright);font-size:7.5px;display:flex;align-items:center;padding-left:67px}
</style>
</head>
<body>

<div class="abs logo">
  <div class="logo-name">Tovenly</div>
  <div class="logo-tag">Shop marijuana in style</div>
</div>
<div class="abs ad">Ad goes here</div>

<nav class="abs nav">
  <div class="nav-home">
    <svg width="14" height="13" viewBox="0 0 14 13"><path d="M7 1 1 6.5h2V12h3V8.5h2V12h3V6.5h2z" fill="#fff"/></svg>
  </div>
  <div class="nav-item">BLOG</div>
  <div class="nav-item">MARIJUANA 101</div>
  <div class="nav-item">LEGAL MARIJUANA</div>
  <div class="nav-item" style="border-right:1px solid rgba(255,255,255,.18)">VAPORIZERS</div>
</nav>
<div class="abs search">
  <svg width="9" height="9" viewBox="0 0 9 9"><circle cx="3.8" cy="3.8" r="2.8" fill="none" stroke="#0f8a80" stroke-width="1.4"/><path d="M6 6l2.3 2.3" stroke="#0f8a80" stroke-width="1.5"/></svg>search
</div>
<div class="abs hero" role="img" aria-label="Gloved hands lifting cannabis buds beside stacked wrapped parcels"></div>

<div class="abs main-bg"></div>

<aside class="abs quick">
  <div class="panel-head">QUICK LINKS</div>
  <div class="panel-box">
    <ul>
      <li>Blog</li><li>Marijuana 101</li><li>Legal Marijuana</li><li>Vaporizers</li><li>About Us</li>
      <li>Colorado Stores</li><li>Washington State Stores</li><li>Edibles (Yummy food!)</li>
      <li>Find friends who get high</li><li>Frequently Asked Questions</li><li>Discussion Forum</li>
      <li>Vaporizer Rankings</li><li>Savings Calculator</li>
    </ul>
  </div>
</aside>

<aside class="abs reach">
  <div class="panel-head">REACH US</div>
  <div class="panel-box">
    <svg width="70" height="38" viewBox="0 0 70 38"><rect width="70" height="38" fill="#3cc45a"/><path d="M0 0 35 24 70 0M0 38 27 19M70 38 43 19" fill="none" stroke="#fff" stroke-width="2.5"/></svg>
    <div class="reach-mail">contact@tovenly.com</div>
  </div>
</aside>

<section class="abs botd">
  <div class="panel-head"><div class="botd-label">BLOG OF THE DAY</div><span style="font-size:9.5px">Read more</span></div>
  <div class="panel-box">
    <div class="botd-card"><div class="botd-img" role="img" aria-label="City skyline behind a park and lake" style="background:linear-gradient(#9cc3e6 0%,#c9d9e6 45%,#5f8a4a 75%,#3d6a30 100%)"></div>Map and ranking of Colorado Stores.</div>
    <div class="botd-card"><div class="botd-img" role="img" aria-label="City skyline with a tall observation tower and mountains" style="background:linear-gradient(#b7c6d4 0%,#dfe4ea 45%,#8a939b 75%,#5d666e 100%)"></div>Map of Washington State stores opening in July.</div>
    <div class="botd-card"><div class="botd-img" role="img" aria-label="Dark smoky city skyline with fire" style="background:linear-gradient(#3a3a3a 0%,#555 50%,#2a2623 80%,#6b3a1e 100%)"></div>Thousands Die As Drugs Sweep Washington State.</div>
  </div>
</section>

<section class="abs allblog">
  <div class="panel-head">ALL BLOG
    <div class="pager">
      <svg width="6" height="8"><path d="M6 0v8L0 4z" fill="#fff"/></svg>
      <span class="current">1</span><span>2</span><span>3</span>
      <svg width="6" height="8"><path d="M0 0v8l6-4z" fill="#fff"/></svg>
    </div>
  </div>
</section>

<article class="abs post" style="top:613px">
  <div class="post-img" role="img" aria-label="Man reclining on a couch smoking" style="background:linear-gradient(135deg,#6b5040,#8a6a55 50%,#3c3c44)"></div>
  <h2 class="post-title">New Colorado Springs Smoker Accepting Potential Obesity</h2>
  <p class="post-text" style="top:54px">Stating that legal marijuana is just "too damn convenient" and makes food taste "too damn good," Dale Porter, a 28-year-old mechanic living in Colorado Springs, Colorado, told reporters that he has accepted his fate as a potential fat man and that there's nothing he can do to stop it.</p>
</article>

<article class="abs post" style="top:758px">
  <div class="post-img" role="img" aria-label="Young man in a printed t-shirt reacting dramatically" style="background:linear-gradient(135deg,#3a2a22,#7a5a48 45%,#d8d4cc 75%,#4a3a30)"></div>
  <h2 class="post-title">Top 7 Thoughts Everyone Has the First Time They Get High</h2>
  <p class="post-text" style="top:54px">Everyone has a unique story about the thoughts that ran through their head the first time they got high. First-timers experience highs that are more intense than any other they may ever experience in their lives, which makes those thoughts even more real, no matter how silly they may be. Here are the top 7 thoughts people have the first time they smoke weed.</p>
</article>

<article class="abs post" style="top:904px;height:134px">
  <div class="post-img" role="img" aria-label="Close-up of a frosty cannabis plant on a dark background" style="background:radial-gradient(circle at 50% 45%,#e6efe0 0%,#9fb88c 35%,#2d3a22 70%,#111 100%)"></div>
  <h2 class="post-title">The Greatest Strain Names (And What They Are)</h2>
  <p class="post-text" style="top:38px">Everyone has a unique story about the thoughts that ran through their head the first time they got high. First-timers experience highs that are more intense than any other they may ever experience in their lives, which makes those thoughts even more real, no matter how silly they may be. Here are the top 7 thoughts people have the first time they smoke weed.</p>
</article>

<footer class="abs footer">
  <div class="foot-h" style="left:67px">Contact Information</div>
  <div class="foot-small" style="left:68px;top:47px">TOVENLY<br>Lorem Ipsum is therefore always free from repetition</div>
  <div class="foot-small" style="left:68px;top:78px;display:flex;align-items:center;gap:3px">
    <svg width="12" height="12" viewBox="0 0 12 12"><path d="M2.5 1 4.5 3.2 3.4 4.6c.8 1.7 2 2.9 3.8 3.8l1.3-1.1L10.8 9.3 9.6 11C5 10.6 1.4 7 1 2.4z" fill="#fff"/></svg>+0 (000) 000-0000
  </div>
  <div class="divider" style="left:244px"></div>
  <div class="foot-h" style="left:259px">Quick Links</div>
  <div class="foot-small" style="left:259px;top:51px">› Blog<br>› Marijuana 101<br>› Legal Marijuana<br>› Vaporizers</div>
  <div class="foot-small" style="left:347px;top:51px">› About Us<br>› Colorado Stores<br>› Washington State Stores<br>› Edibles (Yummy food!)</div>
  <div class="foot-small" style="left:456px;top:51px">› Find friends who get high<br>› Frequently Asked Questions<br>› Discussion Forum<br>› Vaporizer Rankings</div>
  <div class="divider" style="left:566px"></div>
  <div class="foot-h" style="left:581px">Follow us on</div>
  <div class="social" style="left:581px"></div>
  <div class="social" style="left:607px"></div>
  <div class="social" style="left:634px"></div>
  <div class="social" style="left:660px"></div>
</footer>
<div class="abs copy">Copyright © 2014 Tovenly</div>

</body>
</html>
```